New Infographic Design Project

I need a 1 page Infographic that explains our Velqor Strand offer.

Can you use the following content in the attached document to create a 1 page infographic. The image in the bottom of the document is one of our competitors who is offering the same thing, this image is only provided for inspiration and ideas as we need ours to be based on the content of the document and aligned with the Bruvell Brand

```html
<!DOCTYPE html>
<html lang="en">
<head>
<meta charset="utf-8">
<title>Data Ready. AI Ready. In 6 Weeks.</title>
<link href="https://fonts.googleapis.com/css2?family=Barlow:wght@400;600;700&family=Barlow+Condensed:wght@600;700&display=swap" rel="stylesheet">
<style>
  :root{
    --ink:#111318;
    --sky:#3b9ad9;
    --panel-a:#e6eaf0;
    --panel-b:#cdd5de;
    --green:#9bc53d;
    --teal:#10b5a4;
    --blue:#40a2dd;
    --indigo:#4464b1;
    --purple:#924ca0;
    --navy:#2d2b80;
    --title-blue:#3c55b0;
    --title-teal:#11aeb0;
    --edge-ink:#343391;
    --white:#ffffff;
  }
  *{box-sizing:border-box;margin:0;padding:0}
  html,body{width:1200px;height:702px;overflow:hidden;background:var(--white)}
  body{font-family:"Barlow",Arial,sans-serif;color:var(--ink)}
  .canvas{position:relative;width:1200px;height:702px;overflow:hidden}

  .intro{position:absolute;left:0;top:0;width:250px;height:702px;background:var(--white)}
  .headline{position:absolute;left:28px;top:74px;font-family:"Barlow Condensed",Arial Narrow,sans-serif;font-weight:700;font-size:51px;line-height:44px;letter-spacing:-.5px}
  .headline .accent{color:var(--sky)}
  .intro-copy{position:absolute;left:28px;top:222px;width:232px;font-size:17px;line-height:21.9px;font-weight:600}

  .backdrop{position:absolute;left:250px;top:0;width:950px;height:702px;background:linear-gradient(160deg,var(--panel-a) 0%,#d8dee6 50%,var(--panel-b) 100%)}

  .edge{position:absolute;left:275px;top:258px;width:232px}
  .edge h2{font-size:20px;font-weight:700;margin-bottom:13px}
  .edge h3{font-size:16.5px;font-weight:700;line-height:19px}
  .edge p{font-size:14px;line-height:17px;margin-bottom:12px}

  .spine{position:absolute;left:603px;top:120px;width:4px;height:540px;background:#b9c0c9}
  .timeline-title{position:absolute;left:740px;top:32px;font-family:"Barlow Condensed",Arial Narrow,sans-serif;font-weight:700;font-size:28px;color:var(--title-blue);letter-spacing:-.2px}
  .timeline-title span{color:var(--title-teal)}

  .week{position:absolute;left:526px;width:460px;height:82px}
  .week svg{position:absolute;left:0;top:0}
  .week-label{position:absolute;left:14px;top:6px;width:96px;text-align:center;font-family:"Barlow Condensed",Arial Narrow,sans-serif;font-weight:700;line-height:1}
  .week-label small{display:block;font-family:"Barlow",Arial,sans-serif;font-size:14px;letter-spacing:2px;font-weight:600}
  .week-label b{display:block;font-size:50px;letter-spacing:-1px;margin-top:-2px}
  .week-copy{position:absolute;left:113px;top:16px;width:330px;height:66px;display:flex;flex-direction:column;justify-content:center;color:var(--white);font-size:12.6px;line-height:14.4px}
  .week-copy strong{font-weight:700;font-size:13px;margin-bottom:1px}

  .extra-title{position:absolute;left:1023px;top:74px;font-family:"Barlow Condensed",Arial Narrow,sans-serif;font-weight:700;font-size:20px;color:var(--edge-ink)}
  .perk{position:absolute;left:1013px;width:163px;background:var(--white);border-radius:12px;box-shadow:3px 3px 5px rgba(40,50,70,.28);padding:0 10px 0 16px;font-size:13.4px;line-height:15.5px;display:flex;flex-direction:column;justify-content:center}
  .perk strong{font-weight:700}
</style>
</head>
<body>
<main class="canvas">
  <section class="intro">
    <h1 class="headline">DATA READY.<br>AI READY.<br><span class="accent">IN 6 WEEKS.</span></h1>
    <p class="intro-copy">Your long-term strategic data partner We start with a Business Data Assessment or Strand Deployment Assessment to pinpoint the highest-value use cases, the biggest data risks, and the fastest path to impact. We stand up a governed Velqor Strand foundation using repeatable ingestion, validation, and common data model patterns, so your reporting scales cleanly and your AI initiatives provide business value.</p>
  </section>

  <div class="backdrop" role="img" aria-label="Soft blue-grey backdrop of faint flowing digital data characters"></div>

  <section class="edge">
    <h2>The Bruvell Edge</h2>
    <h3>Quality-first delivery</h3>
    <p>Automated validation, data tests, and “quality gates” that stop bad data upstream.</p>
    <h3>Data products, not datasets</h3>
    <p>Clear ownership, SLAs, versioning, and reusable, consumable outputs aligned to high impact business outcomes.</p>
    <h3>Governance that doesn’t slow you down</h3>
    <p>Security, access, lineage, and auditability built in from day one.</p>
    <h3>Operate seamlessly</h3>
    <p>CI/CD, monitoring, and cost controls so the platform stays healthy.</p>
  </section>

  <div class="spine"></div>
  <h2 class="timeline-title">6 WEEK TIME <span>TO VALUE</span></h2>

  <div class="week" style="top:51px;--c:var(--green)">
    <svg width="460" height="82" aria-hidden="true"><polygon points="79,16 424,16 452,49 424,82 79,82" fill="var(--c)"/><polygon points="79,67 103,67 79,82" fill="#000" opacity=".22"/><polygon points="21,0 103,0 103,67 0,67" fill="#fff"/></svg>
    <div class="week-label" style="color:var(--c)"><small>WEEK</small><b>01</b></div>
    <div class="week-copy"><strong>Envision &amp; Assess</strong>Use case shortlist and priority based on highest business impact, current-state review, data risk &amp; compliance priorities, target operating model.</div>
  </div>
  <div class="week" style="top:153px;--c:var(--teal)">
    <svg width="460" height="82" aria-hidden="true"><polygon points="79,16 424,16 452,49 424,82 79,82" fill="var(--c)"/><polygon points="79,67 103,67 79,82" fill="#000" opacity=".22"/><polygon points="21,0 103,0 103,67 0,67" fill="#fff"/></svg>
    <div class="week-label" style="color:var(--c)"><small>WEEK</small><b>02</b></div>
    <div class="week-copy"><strong>Architecture &amp; governance design</strong>Landing zone decisions, security and access model, patterns/standards, delivery plan and success metrics.</div>
  </div>
  <div class="week" style="top:255px;--c:var(--blue)">
    <svg width="460" height="82" aria-hidden="true"><polygon points="79,16 424,16 452,49 424,82 79,82" fill="var(--c)"/><polygon points="79,67 103,67 79,82" fill="#000" opacity=".22"/><polygon points="21,0 103,0 103,67 0,67" fill="#fff"/></svg>
    <div class="week-label" style="color:var(--c)"><small>WEEK</small><b>03</b></div>
    <div class="week-copy"><strong>Strand foundation deployed</strong>Workspaces and environments, automation &amp; CI/CD, onboarding playbooks, baseline policies/guardrails.</div>
  </div>
  <div class="week" style="top:357px;--c:var(--indigo)">
    <svg width="460" height="82" aria-hidden="true"><polygon points="79,16 424,16 452,49 424,82 79,82" fill="var(--c)"/><polygon points="79,67 103,67 79,82" fill="#000" opacity=".22"/><polygon points="21,0 103,0 103,67 0,67" fill="#fff"/></svg>
    <div class="week-label" style="color:var(--c)"><small>WEEK</small><b>04</b></div>
    <div class="week-copy"><strong>Data ingestion + validation framework</strong>Reusable ingestion patterns, automated validation, data contracts/SLAs, observability signals and alerting.</div>
  </div>
  <div class="week" style="top:459px;--c:var(--purple)">
    <svg width="460" height="82" aria-hidden="true"><polygon points="79,16 424,16 452,49 424,82 79,82" fill="var(--c)"/><polygon points="79,67 103,67 79,82" fill="#000" opacity=".22"/><polygon points="21,0 103,0 103,67 0,67" fill="#fff"/></svg>
    <div class="week-label" style="color:var(--c)"><small>WEEK</small><b>05</b></div>
    <div class="week-copy"><strong>Scalable common data model</strong>Domain model, master entities, curated layer, semantic modelling patterns that support Lumera BI at scale.</div>
  </div>
  <div class="week" style="top:561px;--c:var(--navy)">
    <svg width="460" height="82" aria-hidden="true"><polygon points="79,16 424,16 452,49 424,82 79,82" fill="var(--c)"/><polygon points="79,67 103,67 79,82" fill="#000" opacity=".22"/><polygon points="21,0 103,0 103,67 0,67" fill="#fff"/></svg>
    <div class="week-label" style="color:var(--c)"><small>WEEK</small><b>06</b></div>
    <div class="week-copy" style="font-size:12px;line-height:14px"><strong>Business outcomes + AI-ready capability</strong>Executive dashboards and priority reports, performance optimisation, hypercare and handover, AI readiness check and pilot plan (predictive analytics and/or secure enterprise LLM).</div>
  </div>

  <h2 class="extra-title">EXTRA EDGE:</h2>
  <div class="perk" style="top:100px;height:143px"><strong>“AI-ready data” guarantee</strong>Every priority dataset ships with validation rules, ownership, lineage, and freshness SLAs before it can power AI.</div>
  <div class="perk" style="top:259px;height:129px"><strong>Cost-to-serve transparency</strong>Show business owners what each product/report costs to run and optimise it continuously.</div>
  <div class="perk" style="top:404px;height:122px"><strong>Change-proof pipelines</strong>Data contracts + automated tests reduce breakages from upstream schema changes.</div>
  <div class="perk" style="top:544px;height:111px"><strong>Governed self-serve</strong>Catalog + certified datasets so teams move faster without creating data chaos.</div>
</main>
</body>
</html>
```